QRV Advisors needs a web site

We need a web site for www.qrvadvisors-example.com. QRV is a mergers and acquisition consulting company that focuses our buyer and seller services on logistics companies. We help put companies together, and help with legal and financial due diligence. We want the web site to express our service and show the logistics components. We want personalized images versus pictures of trucks and airplanes.

Our new logo uses Burgandy and grey colors. Image attached. We are not in to bold, big letters...classy, artistic, low key preferred. Confidentiality, experience, professional are what we want to express on the site.

All we expect for the first part of this project is a home page, and one subpage.  We are budgeting other funds for the technical aspects of the web site

Reason: All that I'm seeing so far is trucks, forklifts and planes. We are a legal mergers and acquisitions firm that focus on logistics. I like some of the images to say logistics, but really want it say legal, financial, and putting companies together. Will pay extra for the sub page if someone can impress us with a home page.

Reason: Swamped with another project at the moment...will work on this over the weekend and provide designer feedback and select final design by Tuesday

```html
<!DOCTYPE html>
<html lang="en">
<head>
<meta charset="utf-8">
<title>QRV Advisors — Home</title>
<link rel="stylesheet" href="https://fonts.googleapis.com/css2?family=Open+Sans:wght@300;400;600&display=swap">
<style>
  :root {
    --page: #eceff3;
    --card: #ffffff;
    --burgundy: #8e1a45;
    --grey-dark: #4a4a4d;
    --grey: #8a8a8e;
    --grey-light: #c9c9cc;
    --blue: #2b8bc9;
    --rule: #dcdfe3;
    --footer: #333236;
    --green: #3bb37a;
    --orange: #ec6a24;
    --amber: #f0a825;
  }
  * { box-sizing: border-box; margin: 0; padding: 0; }
  html, body { width: 1120px; height: 1200px; overflow: hidden; }
  body { background: var(--page); font-family: "Open Sans", Arial, sans-serif; position: relative; color: var(--grey-dark); }
  .abs { position: absolute; }

  /* header */
  .brand { left: 105px; top: 44px; display: flex; align-items: center; gap: 12px; }
  .brand-square { width: 14px; height: 14px; background: var(--burgundy); }
  .brand-name { font-size: 26px; font-weight: 400; color: var(--burgundy); letter-spacing: 0.5px; }
  .nav-item { top: 0; width: 112px; height: 112px; background: var(--card); text-align: center; color: var(--burgundy); font-size: 11px; text-transform: uppercase; padding-top: 28px; }
  .nav-item svg { display: block; margin: 0 auto 12px; }
  .nav-item.is-active { border-bottom: 4px solid var(--grey-dark); }
  .nav-item.is-active::before { content: ""; position: absolute; left: 52px; top: 0; border: 4px solid transparent; border-top-color: var(--grey-dark); }

  /* hero */
  .hero-image { left: 91px; top: 128px; width: 640px; height: 336px; background: linear-gradient(135deg, #5a5046 0%, #8e8577 35%, #5163b4 55%, #c9bfae 80%, #7b6c5a 100%); }
  .hero-panel { left: 731px; top: 128px; width: 296px; height: 336px; background: var(--card); padding: 34px 24px 0 25px; }
  .hero-kicker { display: flex; align-items: center; gap: 9px; font-size: 19px; color: var(--burgundy); padding-bottom: 8px; border-bottom: 1px solid var(--rule); }
  .hero-title { font-size: 31px; font-weight: 300; color: var(--blue); margin-top: 14px; white-space: nowrap; }
  .hero-text { font-size: 12px; line-height: 16px; color: var(--grey); margin-top: 12px; }
  .hero-button { display: inline-block; margin-top: 34px; background: var(--blue); color: #fff; font-size: 15px; padding: 8px 19px; }
  .hero-dots { position: absolute; right: 14px; bottom: 14px; display: flex; gap: 8px; }
  .dot { width: 13px; height: 13px; border-radius: 50%; border: 1px solid var(--grey-light); }
  .dot.is-current { background: var(--blue); border-color: var(--blue); }

  /* core services */
  .services { left: 91px; top: 488px; width: 935px; height: 281px; background: var(--card); border-top: 1px solid var(--rule); border-bottom: 2px solid var(--rule); }
  .advisor-photo { left: 52px; top: 26px; width: 170px; height: 255px; border-radius: 80px 80px 0 0; background: linear-gradient(180deg, #6a4a3a 0%, #d9b9a0 35%, #dfe3ea 60%, #c8cdd6 100%); }
  .section-title { font-size: 20px; color: var(--burgundy); font-weight: 400; }
  .services .section-title { left: 322px; top: 42px; }
  .service { width: 290px; display: flex; gap: 14px; }
  .service-icon { flex: none; width: 33px; height: 33px; border-radius: 50%; border: 2px solid; display: flex; align-items: center; justify-content: center; }
  .service-name { font-size: 15px; color: var(--burgundy); white-space: nowrap; }
  .service-text { font-size: 12px; line-height: 16px; color: var(--grey); margin-top: 2px; }

  /* clients */
  .clients { left: 91px; top: 797px; width: 935px; height: 277px; background: var(--card); }
  .clients .section-title { width: 100%; text-align: center; top: 18px; }
  .client { width: 200px; height: 40px; text-align: center; font-size: 26px; font-weight: 600; color: var(--grey-light); display: flex; justify-content: center; align-items: center; gap: 8px; white-space: nowrap; }
  .client-mark { flex: none; width: 14px; height: 14px; border-radius: 50%; background: var(--grey-light); }

  /* footer */
  .footer { left: 0; top: 1074px; width: 1120px; height: 126px; background: var(--footer); color: #fff; }
  .footer-links { left: 94px; top: 46px; font-size: 10px; text-transform: uppercase; }
  .footer-legal { left: 94px; top: 70px; font-size: 10px; }
  .social { top: 46px; width: 30px; height: 30px; border-radius: 50%; border: 2px solid #fff; }
</style>
</head>
<body>

<header>
  <div class="abs brand"><span class="brand-square"></span><span class="brand-name">QRV Advisors</span></div>

  <nav>
    <div class="abs nav-item is-active" style="left:533px">
      <svg width="34" height="28" viewBox="0 0 34 28"><path d="M17 2 L32 15 L28 15 L28 27 L20 27 L20 19 L14 19 L14 27 L6 27 L6 15 L2 15 Z" fill="#5f5f63"/></svg>Home
    </div>
    <div class="abs nav-item" style="left:661px">
      <svg width="34" height="30" viewBox="0 0 34 30"><path d="M9 1 H21 L27 7 V29 H9 Z" fill="none" stroke="#5f5f63" stroke-width="2"/><path d="M13 13 H23 M13 18 H23 M13 23 H23" stroke="#5f5f63" stroke-width="2"/></svg>About
    </div>
    <div class="abs nav-item" style="left:789px">
      <svg width="40" height="30" viewBox="0 0 40 30"><rect x="3" y="5" width="24" height="23" rx="3" fill="none" stroke="#5f5f63" stroke-width="2"/><path d="M16 20 L34 2 L38 6 L20 24 L15 25 Z" fill="#5f5f63"/></svg>Service
    </div>
    <div class="abs nav-item" style="left:917px">
      <svg width="40" height="30" viewBox="0 0 40 30"><rect x="2" y="3" width="36" height="24" rx="2" fill="none" stroke="#5f5f63" stroke-width="2.5"/><path d="M3 4 L20 17 L37 4" fill="none" stroke="#5f5f63" stroke-width="2.5"/></svg>Contact
    </div>
  </nav>
</header>

<section>
  <div class="abs hero-image" role="img" aria-label="Photo of a passenger aircraft under maintenance in a hangar"></div>
  <div class="abs hero-panel">
    <div class="hero-kicker">
      <svg width="16" height="16" viewBox="0 0 16 16"><circle cx="8" cy="8" r="7" fill="none" stroke="#c9c9cc"/><path d="M4 8 H11 M8 5 L11 8 L8 11" fill="none" stroke="#c9c9cc" stroke-width="1.3"/></svg>
      SERVICES
    </div>
    <div class="hero-title">PERFECT CHOICE</div>
    <p class="hero-text">Proin gravida nibh vel velit auctor aliquet. Aenean sollicitudin, lorem quis bibendum auctor, nisi elit consequat ipsum. Duis sedt nibh vulputate cursus a sit.</p>
    <span class="hero-button">Read More</span>
    <div class="hero-dots"><span class="dot"></span><span class="dot is-current"></span><span class="dot"></span></div>
  </div>
</section>

<section class="abs services">
  <div class="abs advisor-photo" role="img" aria-label="Portrait of a smiling advisor in a light suit with arms folded"></div>
  <h2 class="abs section-title">OUR CORE SERVICES</h2>

  <div class="abs service" style="left:320px;top:97px">
    <span class="service-icon" style="border-color:var(--green)"><svg width="18" height="16" viewBox="0 0 18 16"><path d="M4 13 A4 4 0 0 1 4 5 A5 5 0 0 1 14 5 A4 4 0 0 1 14 13 Z" fill="#3bb37a"/><path d="M9 6 V11 M6.5 9 L9 11.5 L11.5 9" stroke="#fff" stroke-width="1.6" fill="none"/></svg></span>
    <div><div class="service-name">Lorem ipsum dolor sit</div><p class="service-text">Lorem ipsum dolor sit amet, consectetur adipiscing elit. Phasellus vitae dui ligula.</p></div>
  </div>
  <div class="abs service" style="left:643px;top:97px">
    <span class="service-icon" style="border-color:var(--blue)"><svg width="16" height="16" viewBox="0 0 16 16"><path d="M6 1 H10 V6 L14 14 H2 L6 6 Z" fill="#2b8bc9"/></svg></span>
    <div><div class="service-name">Etiam eget porttitor enim</div><p class="service-text">Lorem ipsum dolor sit amet, consectetur adipiscing elit. Phasellus vitae dui ligula.</p></div>
  </div>
  <div class="abs service" style="left:320px;top:179px">
    <span class="service-icon" style="border-color:var(--orange)"><svg width="16" height="16" viewBox="0 0 16 16"><path d="M2 2 V15" stroke="#ec6a24" stroke-width="2"/><path d="M3 2 H14 L11 6 L14 10 H3 Z" fill="#ec6a24"/></svg></span>
    <div><div class="service-name">Fusce egestas ultricies</div><p class="service-text">Lorem ipsum dolor sit amet, consectetur adipiscing elit. Phasellus vitae dui ligula.</p></div>
  </div>
  <div class="abs service" style="left:643px;top:179px">
    <span class="service-icon" style="border-color:var(--amber)"><svg width="14" height="18" viewBox="0 0 14 18"><circle cx="7" cy="7" r="5.5" fill="none" stroke="#f0a825" stroke-width="1.6"/><path d="M5 13 H9 M5 15.5 H9" stroke="#f0a825" stroke-width="1.6"/></svg></span>
    <div><div class="service-name">Donec convallis arcu id lectus</div><p class="service-text">Lorem ipsum dolor sit amet, consectetur adipiscing elit. Phasellus vitae dui ligula.</p></div>
  </div>
</section>

<section class="abs clients">
  <h2 class="abs section-title">OUR CLIENTS</h2>
  <div class="abs client" style="left:30px;top:75px">Northbay</div>
  <div class="abs client" style="left:249px;top:75px"><span class="client-mark"></span>Verdant</div>
  <div class="abs client" style="left:487px;top:75px">Castlerow</div>
  <div class="abs client" style="left:705px;top:75px"><span class="client-mark"></span>Homestead</div>
  <div class="abs client" style="left:30px;top:176px">Bytefield</div>
  <div class="abs client" style="left:249px;top:176px"><span class="client-mark"></span>Crafton</div>
  <div class="abs client" style="left:487px;top:176px"><span class="client-mark"></span>Trueline</div>
  <div class="abs client" style="left:705px;top:176px">Tablefare</div>
</section>

<footer class="abs footer">
  <div class="abs footer-links">Home &nbsp;•&nbsp; About &nbsp;•&nbsp; Services &nbsp;•&nbsp; Contact</div>
  <div class="abs footer-legal">Design © 2014. All right reserved &nbsp;•&nbsp; Privacy Policy</div>
  <span class="abs social" style="left:899px;background:#a3182c"></span>
  <span class="abs social" style="left:944px;background:#2c3f7a"></span>
  <span class="abs social" style="left:992px;background:#2a6fb8"></span>
</footer>

</body>
</html>
```